Business Card Design

We have recently seen two business cards that caught our attention and think the designs would work for us. We are an accounting firm that serves small businesses in a variety of industries. Attached are the two business card that inspired us along with very rough layouts. We would like to see a professional layout using our company information.

Industry/Entity Type

Accounting

Contact Information for Business Card

Company Name - Dalworth Pryce
Address - 4180 Brambleton Lane, Suite 310, Houston, TX 77051
713-508-9627 - Main
281-369-0714 - Fax

Team Member Names, emails and phone numbers (see attachment)

```html
<!DOCTYPE html>
<html lang="en">
<head>
<meta charset="utf-8">
<title>Dalworth Pryce — Business Card</title>
<link rel="stylesheet" href="https://fonts.googleapis.com/css2?family=Crimson+Text:wght@400&display=swap">
<style>
  :root {
    --page-bg: #e9e7e3;
    --card-bg: #ffffff;
    --ink: #1c1c1c;
    --ink-soft: #8e8e8e;
    --mark-grey: #b4b4b4;
  }
  * { margin: 0; padding: 0; box-sizing: border-box; }
  html, body {
    width: 1200px;
    height: 1000px;
    overflow: hidden;
    background: var(--page-bg);
  }
  body {
    font-family: "Crimson Text", Georgia, serif;
    color: var(--ink);
  }
  .business-card {
    position: absolute;
    left: 60px;
    top: 145px;
    width: 1080px;
    height: 711px;
    background: var(--card-bg);
    box-shadow: 0 6px 18px rgba(0,0,0,0.18);
  }
  .brand-square {
    position: absolute;
    left: 516px;
    top: 150px;
    width: 100px;
    height: 100px;
    background: var(--mark-grey);
  }
  .brand-name {
    position: absolute;
    left: 0;
    width: 1132px;
    top: 268px;
    text-align: center;
    font-size: 48px;
    line-height: 1;
    color: var(--ink);
  }
  .divider {
    position: absolute;
    left: 546px;
    top: 340px;
    width: 12px;
    height: 334px;
  }
  .person {
    position: absolute;
    right: 550px;
    top: 414px;
    text-align: right;
  }
  .person-name {
    font-size: 66px;
    line-height: 66px;
    color: var(--ink);
  }
  .person-title {
    margin-top: 2px;
    margin-right: 11px;
    font-size: 29px;
    line-height: 30px;
    color: var(--ink-soft);
  }
  .contact {
    position: absolute;
    left: 613px;
    top: 396px;
    font-size: 29px;
    color: var(--ink);
  }
  .contact-address p { line-height: 38px; }
  .contact-phones { margin-top: 10px; }
  .contact-phones p { line-height: 38px; }
  .phone-label { color: var(--ink-soft); }
</style>
</head>
<body>
  <main class="business-card">
    <div class="brand-square" aria-hidden="true"></div>
    <div class="brand-name">Dalworth Pryce</div>

    <svg class="divider" viewBox="0 0 12 334" aria-hidden="true">
      <path d="M6 0 C9 60 9 274 6 334 C3 274 3 60 6 0 Z" fill="var(--ink)"/>
    </svg>

    <section class="person">
      <h1 class="person-name" style="font-weight:400">Marisol Fenwick</h1>
      <p class="person-title">Account Manager</p>
    </section>

    <section class="contact">
      <div class="contact-address">
        <p>4180 Brambleton Lane, Suite 310</p>
        <p>Houston, TX 77051</p>
      </div>
      <div class="contact-phones">
        <p>713-508-9627 – <span class="phone-label">Main</span></p>
        <p>713-620-4471 – <span class="phone-label">Direct</span></p>
        <p>832-557-0382 - <span class="phone-label">Mobile</span></p>
      </div>
    </section>
  </main>
</body>
</html>
```